Manufacturing Company WordPress Website Design

Looking for a modern WordPress design for a manufacturer of oil separation and coolant recycling products called BrightVane. This is a business-to-business marketer in the industrial manufacturing sector. BrightVane sells to CNC manufacturing companies and their products are known as some of the best tools in the world for skimming and separating floating oils, metallic fines, and other contaminants from industrial process fluids.

The winning design will be based on a responsive WP theme. Include the theme name if your design is selected by the client. Provide Home, Product and Case Study page views with your submission.

THE BRIGHTVANE BRAND
The BrightVane brand is all about connection and partnership. They are down-to-earth, relatable, helpful and fun to hang out with. The brand voice is humble, authentic and helpful and they are driven by connection, togetherness and inclusion.

The BrightVane target audience is plant managers, enterprise engineers and business owners in CNC machining manufacturing companies across a variety of industries (automotive, aerospace, energy, medical and transportation).

BrightVane is looking for a clean, modern website that better represents their brand with a more polished and professional design. It should be:
- responsive and mobile-friendly
- easily findable for key search criteria
- a source for improved lead generation for prospective sales
- more easily editable

A design that is oriented toward these goals will be selected as the winner.

The winning designer may be chosen to code the website, or to code the initial pages in the concept design.

Current Website:
https://brightvane-example.com/index.html

Competitors:
https://www.tovlex-example.com/
https://www.mundrel-example.com/
https://www.kelvaro-example.com/

Sites We Like:
https://northgatesteelworks-example.com/
- we like the clean layout of the home page in a grid-like design, simple header and footer, the parallax scrolling, and the mobile responsiveness.

https://www.tovlex-example.com/fluid-filtration/sentinel-coolant-recycling-systems/
- we like the way the content is presented on the Tovlex product page - specifically, we like the use of the tabs below the main product images to present a lot of content without it looking overwhelmingly busy.

https://dunmorepanel-example.com/healthcare/westbrook-care-hospital/
- we like the way Dunmore Panel presents their cases studies with a combination of useful information highlighted by informative icons and pictures to present key statistics in the case study. We would like the BrightVane case studies to almost feel like an infographic presentation on the website.

Target Market(s)

Industry/Entity Type

Industrial

Coding

Coded - Design and coding required

Number of Pages Required

3 page

Font styles to use
Sans Serif
Other font styles liked:
• DINPro is used on all collateral - see brand guidelines

Requirements
Must have
• See the brand guidelines file attached for colors and logo usage

```html
<!DOCTYPE html>
<html lang="en">
<head>
<meta charset="utf-8">
<title>BrightVane — Contaminant Control for Industrial Fluids</title>
<link href="https://fonts.googleapis.com/css2?family=Open+Sans:wght@400;600;700&family=Ubuntu:wght@500;700&display=swap" rel="stylesheet">
<style>
:root{
  --navy:#0d3b75;
  --navy-deep:#0b376b;
  --green:#86bc24;
  --text:#555b63;
  --muted:#8a9098;
  --line:#e3e5e8;
  --panel:#f3f4f5;
  --white:#ffffff;
}
*{box-sizing:border-box;margin:0;padding:0}
html,body{width:1200px;height:3587px;overflow:hidden}
body{position:relative;background:var(--white);font-family:"Open Sans",Arial,sans-serif;color:var(--text)}
.abs{position:absolute}
.heading{font-family:"Ubuntu","Open Sans",sans-serif;font-weight:700;color:var(--navy)}
.btn{position:absolute;display:flex;align-items:center;justify-content:center;border-radius:20px;font-size:12px;font-weight:700;letter-spacing:.3px;text-transform:uppercase;white-space:nowrap}
.btn-navy{background:var(--navy);color:var(--white)}
.btn-green{background:var(--green);color:var(--white)}
.btn-outline{border:1.5px solid var(--navy);color:var(--navy);background:var(--white);font-size:11px}

/* header */
.site-header{position:absolute;left:0;top:0;width:1200px;height:93px;background:var(--white)}
.brand{position:absolute;left:97px;top:22px;display:flex;align-items:center;gap:10px}
.brand-mark{width:50px;height:50px;border-radius:50%;background:var(--navy)}
.brand-name{font-family:"Ubuntu",sans-serif;font-weight:700;font-size:28px;color:var(--navy)}
.badge{position:absolute;left:517px;top:16px;width:60px;height:60px;border-radius:50%;border:3px solid #555;background:#eee}
.contact-item{position:absolute;top:37px;display:flex;align-items:center;gap:7px;font-size:12.5px;color:#333;white-space:nowrap}
.nav{position:absolute;left:0;top:93px;width:1200px;height:41px;background:var(--green)}
.nav a{position:absolute;top:13px;font-size:12px;font-weight:600;color:var(--white);text-decoration:none;transform:translateX(-50%);white-space:nowrap}
.nav a.active{color:var(--navy);border-bottom:1.5px solid var(--navy);padding-bottom:2px}

/* hero */
.hero{position:absolute;left:0;top:134px;width:1200px;height:487px;background:linear-gradient(100deg,#4a4a4a 0%,#6a5c52 25%,#585d63 55%,#3f4247 100%)}
.hero-shade{position:absolute;inset:0;background:rgba(20,25,35,.45)}
.hero h1{position:absolute;left:0;width:1200px;top:186px;text-align:center;font-family:"Open Sans",sans-serif;font-weight:700;font-size:25px;color:var(--white)}
.hero p{position:absolute;left:380px;width:440px;top:230px;text-align:center;font-size:14px;line-height:19px;color:var(--white)}
.dots{position:absolute;display:flex;gap:10px}

/* services */
.services-bg{position:absolute;left:0;top:621px;width:1200px;height:882px;background:var(--panel)}
.card{position:absolute;left:97px;top:621px;width:1004px;height:807px;background:var(--white);box-shadow:0 4px 18px rgba(0,0,0,.08)}
.media{position:absolute;background:linear-gradient(135deg,#f4f4f4,#dedfe2)}
.svc-title{position:absolute;font-family:"Open Sans",sans-serif;font-weight:700;font-size:16px;color:var(--navy)}
.svc-text{position:absolute;font-size:11.5px;line-height:18px;color:var(--muted)}
.view-all{position:absolute;left:106px;top:1377px;width:988px;height:44px;background:var(--navy);color:var(--white);font-size:13px;display:flex;align-items:center;justify-content:center}

/* section titles */
.section-title{position:absolute;left:0;width:1200px;text-align:center;font-size:27px}
.section-title span{color:var(--navy);font-weight:400;margin:0 10px}

.logo-box{position:absolute;top:1651px;width:183px;height:86px;border:1px solid var(--line);display:flex;align-items:center;justify-content:center;gap:8px;font-family:"Open Sans",sans-serif;font-weight:700;font-size:14px;color:var(--navy);white-space:nowrap}
.logo-box i{width:14px;height:14px;border-radius:50%;background:var(--navy);display:block}

/* roi */
.roi{position:absolute;left:0;top:1812px;width:1200px;height:340px;background:linear-gradient(90deg,#c9c7c2 0%,#a6a39e 45%,#7c7a76 75%,#5d6166 100%)}
.roi-card{position:absolute;left:97px;top:1842px;width:461px;height:279px;background:var(--white)}

/* testimonials */
.quote-circle{position:absolute;left:567px;top:2292px;width:66px;height:66px;border-radius:50%;background:#eff1f3;display:flex;align-items:center;justify-content:center}
.testimonial{position:absolute;left:235px;width:730px;top:2384px;text-align:center;font-size:13px;line-height:19px;color:#444}

/* quote form */
.quote{position:absolute;left:0;top:2623px;width:1200px;height:423px;background:linear-gradient(90deg,#e2e2e2,#eeeeee 40%,#e4e4e4 70%,#d9d9d9)}
.field{position:absolute;background:var(--white);border:1px solid #dcdcdc;border-radius:18px;font-size:11.5px;color:#9a9a9a;padding:0 15px;display:flex;align-items:center}

/* newsletter */
.newsletter{position:absolute;left:0;top:3046px;width:1200px;height:104px;background:var(--green)}

/* footer */
.footer{position:absolute;left:0;top:3150px;width:1200px;height:395px;background:var(--navy-deep);color:var(--white)}
.foot-h{position:absolute;font-family:"Ubuntu",sans-serif;font-weight:700;font-size:18px;color:var(--green)}
.foot-label{position:absolute;font-size:11.5px;font-weight:700;color:var(--green)}
.foot-line{position:absolute;font-size:12.5px;color:var(--white);display:flex;align-items:center;gap:8px;white-space:nowrap}
.foot-link{position:absolute;left:376px;font-size:13px;color:var(--white)}
.social{position:absolute;top:3461px;width:25px;height:25px;border-radius:50%;border:1.5px solid var(--white)}
.map{position:absolute;left:592px;top:3210px;width:547px;height:284px;background:linear-gradient(135deg,#d9e8c9,#cfe3cc 45%,#b9d4ec 70%,#e4edd8)}
.copyright{position:absolute;left:0;top:3545px;width:1200px;height:42px;background:var(--green);color:var(--white);font-size:12px;display:flex;align-items:center;justify-content:center}
</style>
</head>
<body>

<header class="site-header">
  <div class="brand"><span class="brand-mark"></span><span class="brand-name">BrightVane</span></div>
  <div class="badge" role="img" aria-label="Award badge"></div>
  <div class="contact-item" style="left:596px">
    <svg width="18" height="13" viewBox="0 0 18 13"><rect x="1" y="1" width="16" height="11" fill="none" stroke="#86bc24" stroke-width="1.6"/><path d="M1 1l8 6 8-6" fill="none" stroke="#86bc24" stroke-width="1.6"/></svg>
    sales@brightvane-example.com
  </div>
  <div class="contact-item" style="left:812px">
    <svg width="14" height="14" viewBox="0 0 24 24"><path fill="#86bc24" d="M6.6 10.8a15 15 0 006.6 6.6l2.2-2.2c.3-.3.7-.4 1-.2 1.1.4 2.3.6 3.6.6.6 0 1 .4 1 1V20c0 .6-.4 1-1 1A17 17 0 013 4c0-.6.4-1 1-1h3.5c.6 0 1 .4 1 1 0 1.3.2 2.5.6 3.6.1.3 0 .7-.2 1z"/></svg>
    (555) 014-7320
  </div>
  <div class="btn btn-navy" style="left:930px;top:29px;width:171px;height:34px">Request a Quote</div>
</header>

<nav class="nav">
  <a class="active" style="left:237px">HOME</a>
  <a style="left:326px">PRODUCTS</a>
  <a style="left:425px">BENEFITS</a>
  <a style="left:550px">INDUSTRIES SERVED</a>
  <a style="left:679px">ABOUT US</a>
  <a style="left:807px">SERVICE &amp; SUPPORT</a>
  <a style="left:942px">CONTACT US</a>
</nav>

<section class="hero" role="img" aria-label="Plant engineers in safety vests reviewing a tablet on the shop floor">
  <div class="hero-shade"></div>
  <h1>WHO WE ARE / WHAT WE DO</h1>
  <p>Since 1998, the BrightVane product line has been producing some of the best solutions in the world for the...</p>
  <div class="btn btn-navy" style="left:518px;top:302px;width:163px;height:36px">Learn More</div>
  <div class="dots" style="left:578px;top:445px">
    <svg width="12" height="18" viewBox="0 0 12 18"><path d="M6 1C6 1 1 8 1 12a5 5 0 0010 0C11 8 6 1 6 1z" fill="none" stroke="#86bc24" stroke-width="1.6"/></svg>
    <svg width="12" height="18" viewBox="0 0 12 18"><path d="M6 1C6 1 1 8 1 12a5 5 0 0010 0C11 8 6 1 6 1z" fill="#86bc24"/></svg>
    <svg width="12" height="18" viewBox="0 0 12 18"><path d="M6 1C6 1 1 8 1 12a5 5 0 0010 0C11 8 6 1 6 1z" fill="none" stroke="#86bc24" stroke-width="1.6"/></svg>
  </div>
</section>

<div class="services-bg"></div>
<svg class="abs" style="left:0;top:621px" width="1200" height="120" viewBox="0 0 1200 120"><polygon points="0,0 1200,0 1200,10 0,95" fill="#ffffff"/></svg>

<section class="card">
  <div class="media" style="left:9px;top:8px;width:305px;height:235px" role="img" aria-label="Blue coolant recycling system unit with drum"></div>
  <h3 class="svc-title" style="left:372px;top:57px">Coolant Recycling Systems</h3>
  <p class="svc-text" style="left:372px;top:99px;width:560px">The FlowCycle™ Coolant Recycling Systems are based on decades-long successful fluid treatment practices, using the award-winning, multipatented BrightVane® Systems approach to solving problems...</p>
  <div class="btn btn-outline" style="left:373px;top:181px;width:127px;height:32px">Learn More</div>

  <h3 class="svc-title" style="left:63px;top:309px">Magnetic Separators</h3>
  <p class="svc-text" style="left:63px;top:351px;width:560px">BrightVane magnetic separators fit with our core philosophies: providing products that eliminate the use of filter consumables, are easy to implement, simple to operate, and require minimal maintenance.</p>
  <div class="btn btn-outline" style="left:64px;top:433px;width:126px;height:32px">Learn More</div>
  <div class="media" style="left:692px;top:260px;width:304px;height:235px" role="img" aria-label="Two clear magnetic separator canisters"></div>

  <div class="media" style="left:9px;top:512px;width:305px;height:235px" role="img" aria-label="Stainless oil water separator with pumps"></div>
  <h3 class="svc-title" style="left:372px;top:561px">Oil Water Separators</h3>
  <p class="svc-text" style="left:372px;top:603px;width:440px">The BrightVane "non-clogging" design allows for the separation of oils and settling of solids in one step.</p>
  <div class="btn btn-green" style="left:373px;top:685px;width:127px;height:32px;font-size:11px">Learn More</div>
</section>
<div class="view-all">VIEW ALL SERVICES</div>

<h2 class="section-title heading" style="top:1572px"><span>–</span>Trusted By<span>–</span></h2>
<svg class="abs" style="left:992px;top:1581px" width="20" height="20" viewBox="0 0 20 20"><circle cx="10" cy="10" r="9" fill="none" stroke="#c8cbd0" stroke-width="1.4"/><path d="M14 10H6m3-3l-3 3 3 3" fill="none" stroke="#c8cbd0" stroke-width="1.4"/></svg>
<svg class="abs" style="left:1024px;top:1581px" width="20" height="20" viewBox="0 0 20 20"><circle cx="10" cy="10" r="9" fill="none" stroke="#0d3b75" stroke-width="1.4"/><path d="M6 10h8m-3-3l3 3-3 3" fill="none" stroke="#0d3b75" stroke-width="1.4"/></svg>
<div class="abs" style="left:1059px;top:1583px;font-size:12px;color:var(--navy);text-decoration:underline">View All</div>

<div class="logo-box" style="left:97px"><i></i>Harlow Motors</div>
<div class="logo-box" style="left:303px"><i></i>Greenfield Tractor</div>
<div class="logo-box" style="left:509px"><i></i>Bavaro Auto</div>
<div class="logo-box" style="left:714px"><i></i>Ironhorse Cycles</div>
<div class="logo-box" style="left:919px"><i></i>Bolten Works</div>

<section class="roi" role="img" aria-label="Hand typing on a desk calculator beside a laptop"></section>
<div class="roi-card">
  <h2 class="heading" style="position:absolute;left:44px;top:46px;font-size:26px;font-weight:500">ROI Calculator</h2>
  <p style="position:absolute;left:46px;top:102px;width:370px;font-size:11.5px;line-height:18px;color:var(--text)">By drastically reducing coolant costs and the cost of waste removal, our typical systems pay for themselves in 6-9 months. Check ot our ROI calculator to determine how much you can savie with our coolant recycling systems.</p>
  <div class="btn btn-green" style="left:46px;top:194px;width:247px;height:33px;font-size:11.5px">Calculate Your Savings Now</div>
</div>

<h2 class="section-title heading" style="top:2219px"><span>–</span>Testimonials<span>–</span></h2>
<div class="quote-circle">
  <svg width="30" height="24" viewBox="0 0 30 24"><path fill="#86bc24" d="M2 24V14C2 6 6 1 13 0v5c-4 1-5 4-5 8h5v11zm16 0V14c0-8 4-13 11-14v5c-4 1-5 4-5 8h5v11z"/></svg>
</div>
<p class="testimonial">Lorem Ipsum is simply dummy text of the printing and typesetting industry. Lorem Ipsum has been the industry's standard dummy text ever since the 1500s, when an unknown printer took a galley of type and scrambled it to make a type specimen book. It has survived not only five centuries, but also...</p>
<div class="abs" style="left:497px;top:2467px;display:flex;align-items:center;gap:8px;font-size:11px;color:#333;white-space:nowrap">
  <svg width="14" height="14" viewBox="0 0 14 14"><rect x="1" y="2" width="12" height="11" fill="none" stroke="#86bc24" stroke-width="1.5"/><path d="M1 5h12M4 0v3M10 0v3" stroke="#86bc24" stroke-width="1.5"/></svg>
  17 Dec, 2020 <span style="color:#ccc;margin:0 10px">|</span><b style="font-size:12px">Dana Ortell</b>
</div>
<svg class="abs" style="left:545px;top:2532px" width="110" height="16" viewBox="0 0 110 16"><circle cx="8" cy="8" r="3.5" fill="#c5c8cc"/><circle cx="31" cy="8" r="3.5" fill="#c5c8cc"/><circle cx="55" cy="8" r="6" fill="none" stroke="#86bc24" stroke-width="1.5"/><circle cx="55" cy="8" r="3.5" fill="#86bc24"/><circle cx="78" cy="8" r="3.5" fill="#c5c8cc"/><circle cx="101" cy="8" r="3.5" fill="#c5c8cc"/></svg>

<section class="quote" role="img" aria-label="Faded greyscale photo of workers in a plant"></section>
<h2 class="section-title heading" style="top:2688px"><span>–</span>Request a Quote<span>–</span></h2>
<div class="field" style="left:322px;top:2769px;width:270px;height:36px">Name</div>
<div class="field" style="left:322px;top:2822px;width:270px;height:36px">Phone</div>
<div class="field" style="left:322px;top:2875px;width:270px;height:36px">Email</div>
<div class="field" style="left:322px;top:2926px;width:270px;height:36px;justify-content:space-between">Select Your Services
  <svg width="9" height="6" viewBox="0 0 9 6"><path d="M1 1l3.5 3.5L8 1" fill="none" stroke="#888" stroke-width="1.3"/></svg></div>
<div class="field" style="left:607px;top:2769px;width:270px;height:140px;align-items:flex-start;padding-top:11px;border-radius:14px">Message</div>
<div class="btn btn-navy" style="left:607px;top:2926px;width:270px;height:36px;justify-content:flex-start;padding-left:40px">Get a Free Consultation</div>

<section class="newsletter">
  <svg class="abs" style="left:223px;top:20px" width="58" height="62" viewBox="0 0 58 62"><path d="M3 26l26-20 26 20v32H3z" fill="none" stroke="#0d3b75" stroke-width="2.2"/><path d="M3 26l26 18 26-18M3 58l20-16M55 58L35 42" fill="none" stroke="#0d3b75" stroke-width="2.2"/><rect x="13" y="10" width="32" height="22" fill="#86bc24" stroke="#0d3b75" stroke-width="2"/><path d="M18 17h22M18 23h16" stroke="#0d3b75" stroke-width="2"/></svg>
  <div class="abs heading" style="left:299px;top:30px;font-size:16px;font-family:'Open Sans',sans-serif;white-space:nowrap">STAY UP TO DATE WITH BRIGHTVANE</div>
  <div class="abs" style="left:299px;top:53px;font-size:12.5px;color:var(--navy)">Sign up to get our Newsletter</div>
  <div class="field" style="left:639px;top:32px;width:376px;height:37px;border:2px solid var(--white);padding-left:20px">Enter email address</div>
  <div class="btn btn-navy" style="left:877px;top:34px;width:136px;height:33px;font-size:11px">Subscribe Now</div>
</section>

<footer class="footer">
  <div class="foot-h" style="left:97px;top:72px">Conatct info</div>
  <div class="foot-label" style="left:97px;top:113px">CALL US:</div>
  <div class="foot-line" style="left:97px;top:136px"><svg width="12" height="12" viewBox="0 0 24 24"><path fill="#86bc24" d="M6.6 10.8a15 15 0 006.6 6.6l2.2-2.2c.3-.3.7-.4 1-.2 1.1.4 2.3.6 3.6.6.6 0 1 .4 1 1V20c0 .6-.4 1-1 1A17 17 0 013 4c0-.6.4-1 1-1h3.5c.6 0 1 .4 1 1 0 1.3.2 2.5.6 3.6.1.3 0 .7-.2 1z"/></svg>+1 555-014-7320</div>
  <div class="foot-line" style="left:97px;top:160px"><svg width="12" height="12" viewBox="0 0 12 12"><rect x="1" y="4" width="10" height="7" fill="#86bc24"/><rect x="3" y="1" width="6" height="3" fill="none" stroke="#86bc24" stroke-width="1.2"/></svg>+1 555-014-2891</div>
  <div class="foot-line" style="left:97px;top:183px"><svg width="12" height="9" viewBox="0 0 12 9"><rect width="12" height="9" fill="#86bc24"/><path d="M0 0l6 5 6-5" fill="none" stroke="#0b376b" stroke-width="1"/></svg>sales@brightvane-example.com</div>
  <div class="foot-label" style="left:97px;top:226px">ADDRESS:</div>
  <div class="foot-line" style="left:97px;top:248px;display:block;line-height:20px">1480 Carrow Lane<br>Riverton, State 00000, USA</div>

  <div class="foot-h" style="left:376px;top:72px">Quick Link</div>
  <div class="foot-link" style="top:116px;color:var(--green);text-decoration:underline">Home</div>
  <div class="foot-link" style="top:146px">Products</div>
  <div class="foot-link" style="top:176px">Benefits</div>
  <div class="foot-link" style="top:206px">Industries Served</div>
  <div class="foot-link" style="top:236px">About Us</div>
  <div class="foot-link" style="top:266px">Service &amp; Support</div>
  <div class="foot-link" style="top:296px">Conatct Us</div>
</footer>
<div class="social" style="left:99px" role="img" aria-label="Video channel"></div>
<div class="social" style="left:140px;border-color:var(--green)" role="img" aria-label="Professional network"></div>
<div class="social" style="left:180px" role="img" aria-label="Photo sharing"></div>
<div class="map" role="img" aria-label="Regional map showing office locations"></div>

<div class="copyright">Copyright © 2021 BrightVane. All Rights Reserved</div>

</body>
</html>
```